World's first Total Sustainability Management System needs brochure

DESIGN BRIEF
1. HISTORY
The company is a new company but has very quickly gained global recognition by international bodies such as the UN and is already operating globally.
2. PROBLEM STATEMENT + MESSAGE
The system provides management of a wide range of problems in the business, and a significant number of benefits from reduced costs, to better risk management, improved compliance, recognition, differentiation strategy, reporting etc.
Corvane Ledger needs to communicate this message simply.
The target audience is industry leaders WHO ARE ALREADY commited to CSR/ Sustainability.
The message is that Corvane Ledger can help them do it better, reduce costs, improve risk management and provide them with a return on their investment in sustainability/ social resonsibility.
Website: www.clgassure.example
3. GOALS
To position Corvane Ledger as distinct, elite management system. It is much much more than a mere reporting system or corporate giving program. Rather, it provides management with a whole strategy and range of tools for managing the soft side of the business.
4. DESIRED TEXT
What does sustainability or social investment mean to you?
Many businesses see it as charitable giving or an annual report or an environmental program. International best practice describes it more broadly and comprehensively. It includes such things as workplace safety, anti-corruption and labour.
What do you currently receive for your social investment?
a) report
b) community recognition
c) certificate
Can you do it better and get a better return on your social investment?
The Corvane Ledger CSR Management System is built specifically to enhance business performance using socially responsibility principles. It not only provides reporting, recognition, certification, but provides a return on investment. It is web based system, provides complete management system and comprehensive framework to drive improvement and social responsibility throughout your business.
Corvane Ledger, a UN recognised business, provides a comprehensive system for embedding performance enhancing world best practices into your business.

5. COLLATERAL
We would like to see this on a double sided A4 sheet of paper (or 8 ½ x 11)

Isn’t it time you joined world leaders?
Corvane Ledger Assurance Systems
47 Marlow St, Kew Heights, Vic or 8 Tanning Row, London, UK SE9 4QP
Email: info@clgassure.example Email: info@clgassure.example
Phone: +61 3 9415-2783 +44 (0) 20 7316 5527

Reason: The original design brief was inadequate--my apologies. Please have a look and see if this works better for you.

Hello, I have added some details which were unavailable before and committed the funding to the project. Thanks for your interest.

Target Market(s)

This brochure is designed for CEO's and other top level executives who are knowledgeable and interested in social responsibility and sustainability. They are middle aged, are all well educated and socially concerned.

Industry/Entity Type

Sustainability

Font styles to use
Sans Serif

Requirements
Must have
• Must be 2 sided A4 (8.5 x 11).
PLEASE SEE WEBSITE FOR ADDITIONAL INFORMATION www.clgassure.example
Should not have
• It should not over emphasise green/ environmental issues.

```html
<!DOCTYPE html>
<html lang="en">
<head>
<meta charset="utf-8">
<title>Corvane Ledger Assurance Systems – Brochure Spread</title>
<link href="https://fonts.googleapis.com/css2?family=Exo+2:wght@600;700&family=Open+Sans:wght@400;600;700&display=swap" rel="stylesheet">
<style>
  :root {
    --canvas: #e4e4e4;
    --sky-top: #eef0f2;
    --sky-mid: #c9d6e0;
    --sky-blue: #7fa3bf;
    --horizon: #d9c67a;
    --soil: #b8663a;
    --field: #9a9a3a;
    --field-deep: #6f7a2a;
    --brand-blue: #1f6fa0;
    --heading-teal: #1a9aa0;
    --body-text: #3a3f44;
    --tagline: #f3ecc4;
    --white: #ffffff;
  }
  * { box-sizing: border-box; margin: 0; padding: 0; }
  html, body { width: 1200px; height: 842px; overflow: hidden; }
  body {
    background: var(--canvas);
    font-family: "Open Sans", Arial, sans-serif;
    color: var(--body-text);
  }
  .spread {
    position: absolute; left: 5px; top: 0;
    width: 1190px; height: 842px;
    overflow: hidden;
  }
  .landscape-photo {
    position: absolute; inset: 0;
    background:
      linear-gradient(180deg, transparent 0%, transparent 62%, var(--horizon) 66%, var(--soil) 69%, var(--field) 74%, var(--field-deep) 100%),
      linear-gradient(170deg, var(--sky-top) 0%, var(--sky-mid) 30%, var(--sky-blue) 45%, var(--sky-mid) 55%, #e6dcb0 64%);
  }
  .page-fold {
    position: absolute; left: 595px; top: 0; width: 1px; height: 100%;
    background: rgba(0,0,0,0.08);
  }
  .page { position: absolute; top: 0; width: 595px; height: 842px; }
  .page--back { left: 0; }
  .page--front { left: 595px; }

  .brand {
    display: flex; align-items: center; gap: 10px;
  }
  .brand-square {
    width: 34px; height: 34px; background: var(--brand-blue); flex: none;
  }
  .brand-name {
    color: var(--brand-blue); font-family: "Open Sans", Arial, sans-serif;
    font-weight: 600; line-height: 1.05;
  }

  .statement { position: absolute; left: 55px; width: 480px; font-size: 11.5px; line-height: 1.45; }
  .statement h2 {
    font-family: "Exo 2", Arial, sans-serif; font-weight: 700;
    color: var(--heading-teal); font-size: 15px; letter-spacing: 1.5px;
    margin-bottom: 4px;
  }
  .statement p + p { margin-top: 10px; }
  .statement--mission { top: 110px; }
  .statement--vision { top: 385px; }

  .back-brand { position: absolute; left: 55px; top: 500px; }
  .back-brand .brand-name { font-size: 20px; }

  .offices {
    position: absolute; left: 55px; top: 555px; width: 500px;
    display: grid; grid-template-columns: 1fr 1fr; gap: 0 28px;
    font-size: 11px; line-height: 1.4; color: #20262b;
  }
  .offices h3 { font-size: 11.5px; font-weight: 700; }
  .office + .office-postal { margin-top: 10px; }

  .web-link {
    position: absolute; left: 55px; top: 770px;
    display: flex; align-items: center; gap: 10px;
    color: var(--white); font-weight: 700; font-size: 16px; letter-spacing: 0.5px;
  }

  .front-brand { position: absolute; left: 75px; top: 70px; }
  .front-brand .brand-square { width: 48px; height: 48px; }
  .front-brand .brand-name { font-size: 30px; }

  .tagline {
    position: absolute; left: 150px; top: 360px; width: 420px;
    font-family: "Exo 2", Arial, sans-serif; font-weight: 600;
    font-size: 38px; line-height: 1.2; color: var(--tagline);
    text-align: center; letter-spacing: 0.5px;
  }
</style>
</head>
<body>
  <main class="spread">
    <div class="landscape-photo" role="img" aria-label="Photograph of wind turbines standing on a wide green and golden field under a streaked blue and grey sky, spanning both pages"></div>
    <div class="page-fold"></div>

    <section class="page page--back">
      <div class="statement statement--mission">
        <h2>MISSION</h2>
        <p>To enable businesses globally to benefit from implementing effective CSR and to link these businesses together to improve the lives of people in all parts of the planet.</p>
        <p>Corvane Ledger Assurance Systems is dedicated to creating and distributing the world's leading effective CSR tools and systems as widely as possible. To realise its vision and achieve its mission, Corvane Ledger Assurance Systems has created and developed the world's leading CSR tools and systems. Corvane Ledger Assurance Systems currently provides a CSR Management System, a Market and Supply Chain Assurance System, a CSR Evaluation and Transition Tool in addition to consulting, education and various other services.</p>
        <p>Corvane Ledger Assurance Systems is already working with a growing number of businesses committed to socially responsible practices in many countries of the world.</p>
      </div>

      <div class="statement statement--vision">
        <h2>VISION</h2>
        <p>To see business everywhere operating in socially responsible ways.</p>
      </div>

      <div class="brand back-brand">
        <span class="brand-square"></span>
        <span class="brand-name">Corvane Ledger<br>Assurance Systems</span>
      </div>

      <div class="offices">
        <div>
          <div class="office">
            <h3>Melbourne</h3>
            <p>Corvane Ledger Assurance Systems<br>47 Marlow Street<br>Kew Heights, Victoria, Australia 3141<br>Telephone: +61 (0) 3 9415 2783<br>Email: info@clgassure.example</p>
          </div>
          <div class="office-postal">
            <h3>Melbourne Postal Address</h3>
            <p>PO Box 517<br>Kew Heights, Victoria, Australia 3141</p>
          </div>
        </div>
        <div class="office">
          <h3>London</h3>
          <p>Corvane Ledger Assurance Systems<br>8 Tanning Row<br>London, SE9 4QP<br>Telephone: +44 (0) 20 7316 5527<br>Email: info@clgassure.example</p>
        </div>
      </div>

      <div class="web-link">
        <svg width="20" height="20" viewBox="0 0 20 20" aria-hidden="true">
          <g fill="none" stroke="#ffffff" stroke-width="1.5">
            <circle cx="10" cy="10" r="8.5"/>
            <ellipse cx="10" cy="10" rx="4" ry="8.5"/>
            <line x1="1.5" y1="10" x2="18.5" y2="10"/>
          </g>
        </svg>
        <span>www.clgassure.example</span>
      </div>
    </section>

    <section class="page page--front">
      <div class="brand front-brand">
        <span class="brand-square"></span>
        <span class="brand-name">Corvane Ledger<br>Assurance Systems</span>
      </div>
      <h1 class="tagline">Improving Business Performance Through Social Responsibility</h1>
    </section>
  </main>
</body>
</html>
```